Ember Fold Whiskey Label

We are looking for a label to be made for our single batch whiskey. in the attached pdf you will see the lay out of the design. We are going to use a whiskey bottle with a cork. Some of the label you will need to leave some space for hand writing.

Target Market(s)

people who like craft beer and whiskey

Industry/Entity Type

Craft Distillery

Font styles to use
Decorative

Colors

Designer to choose colors to be used in the design.

Requirements
Must have
• room for hand writing informatiom

```html
<!DOCTYPE html>
<html lang="en">
<head>
<meta charset="utf-8">
<title>Ember Fold Whiskey Labels</title>
<link href="https://fonts.googleapis.com/css2?family=Libre+Baskerville:wght@400;700&family=Parisienne&family=Montserrat:wght@400;600&display=swap" rel="stylesheet">
<style>
  :root {
    --page: #ffffff;
    --border: #e9e6df;
    --green-dark: #07140a;
    --green-mid: #1d4a1c;
    --gold-ink: #e2c21c;
    --gold-light: #e9c84a;
    --gold-mid: #c99a1c;
    --gold-deep: #8a6410;
    --black-ink: #151109;
    --silver-hi: #f4f4f2;
    --silver-lo: #c9c9c6;
    --field-ink: #2a2a2a;
  }
  * { box-sizing: border-box; margin: 0; padding: 0; }
  html, body { width: 1200px; height: 1200px; overflow: hidden; background: var(--page); }
  .canvas { position: relative; width: 1200px; height: 1200px; }

  .label {
    position: absolute;
    width: 500px;
    height: 640px;
    border-radius: 34px;
    border: 7px solid var(--border);
    padding: 40px 40px 24px;
    display: flex;
    flex-direction: column;
    align-items: center;
    overflow: hidden;
  }
  .label--green { left: 60px; top: 480px; color: var(--gold-ink); }
  .label--gold { left: 640px; top: 80px; color: var(--black-ink); }

  .label__texture { position: absolute; inset: 0; z-index: 0; }
  .label--green .label__texture {
    background: radial-gradient(ellipse at 30% 40%, var(--green-mid) 0%, #0f2a10 40%, var(--green-dark) 80%);
  }
  .label--gold .label__texture {
    background: radial-gradient(ellipse at 45% 35%, var(--gold-light) 0%, var(--gold-mid) 55%, var(--gold-deep) 100%);
  }
  .label > *:not(.label__texture) { position: relative; z-index: 1; }

  .brand {
    font-family: 'Libre Baskerville', serif;
    font-weight: 700;
    font-size: 44px;
    line-height: 1.12;
    text-align: center;
  }
  .divider { width: 82%; height: 2px; background: currentColor; margin: 14px 0 4px; opacity: .85; }
  .product {
    font-family: 'Parisienne', cursive;
    font-size: 46px;
    line-height: 1.1;
    color: #d9d6cf;
  }
  .label--gold .product { color: var(--black-ink); }
  .divider--short { width: 74%; margin: 4px 0 10px; }
  .spirit-type {
    font-family: 'Libre Baskerville', serif;
    font-weight: 700;
    text-align: center;
    line-height: 1.25;
  }
  .spirit-type__line1 { font-size: 17px; display: block; }
  .spirit-type__line2 { font-size: 23px; display: block; }

  .fields {
    width: 100%;
    margin-top: 14px;
    display: grid;
    grid-template-columns: 1fr 1fr;
    grid-template-rows: 42px 48px 48px 48px;
    gap: 8px 10px;
  }
  .field {
    background: linear-gradient(160deg, var(--silver-hi), var(--silver-lo));
    border-radius: 16px;
    font-family: 'Libre Baskerville', serif;
    font-size: 12px;
    color: var(--field-ink);
    padding: 10px 14px;
  }
  .field--wide { grid-column: 1 / 3; }
  .field--of { grid-column: 2; grid-row: 3 / 5; }

  .maker {
    margin-top: auto;
    width: 100%;
    padding: 0 58px;
    font-family: 'Montserrat', sans-serif;
    text-align: center;
    line-height: 1.35;
    position: relative;
  }
  .maker__intro { font-size: 11px; letter-spacing: .04em; }
  .maker__name { font-size: 13px; font-weight: 600; white-space: nowrap; }
  .maker__address { font-size: 10px; letter-spacing: .02em; white-space: nowrap; }
  .volume {
    position: absolute;
    right: 0;
    bottom: 0;
    font-family: 'Montserrat', sans-serif;
    font-weight: 600;
    font-size: 13px;
    line-height: 1.35;
  }
</style>
</head>
<body>
<main class="canvas">

  <section class="label label--gold">
    <div class="label__texture" role="img" aria-label="Gold foil texture background"></div>
    <h1 class="brand">Iron Spur<br>Distillery</h1>
    <div class="divider"></div>
    <p class="product">Ember Fold</p>
    <div class="divider divider--short"></div>
    <p class="spirit-type"><span class="spirit-type__line1">Spirits Distilled from</span><span class="spirit-type__line2">Malt Mash and Hops</span></p>
    <div class="fields">
      <div class="field field--wide"></div>
      <div class="field">Distillate Source:</div>
      <div class="field">% Alc. by Vol.</div>
      <div class="field">Aged:</div>
      <div class="field field--of">Of:</div>
      <div class="field">Bottle:</div>
    </div>
    <footer class="maker">
      <p class="maker__intro">DISTILLED AND BOTTLED BY</p>
      <p class="maker__name">IRON SPUR DISTILLERY LLC</p>
      <p class="maker__address">48 FOUNDRY LANE, MILLBROOK NY 12545</p>
      <span class="volume">750ML</span>
    </footer>
  </section>

  <section class="label label--green">
    <div class="label__texture" role="img" aria-label="Dark green distressed texture background"></div>
    <h1 class="brand">Iron Spur<br>Distillery</h1>
    <div class="divider"></div>
    <p class="product">Ember Fold</p>
    <div class="divider divider--short"></div>
    <p class="spirit-type"><span class="spirit-type__line1">Spirits Distilled from</span><span class="spirit-type__line2">Malt Mash and Hops</span></p>
    <div class="fields">
      <div class="field field--wide"></div>
      <div class="field">Distillate Source:</div>
      <div class="field">% Alc. by Vol.</div>
      <div class="field">Aged:</div>
      <div class="field field--of">Of:</div>
      <div class="field">Bottle:</div>
    </div>
    <footer class="maker">
      <p class="maker__intro">DISTILLED AND BOTTLED BY</p>
      <p class="maker__name">IRON SPUR DISTILLERY LLC</p>
      <p class="maker__address">48 FOUNDRY LANE, MILLBROOK NY 12545</p>
      <span class="volume">750ML</span>
    </footer>
  </section>

</main>
</body>
</html>
```